Corvane Supplies Business Card

Professional business card that stand out to our potential customers. Front and back with clean modern design

Industry/Entity Type

Oil and gas

Contact Information for Business Card

Name, address, website , office phone and cell number

Requirements
Must have
• Editable files for each employee

```html
<!DOCTYPE html>
<html lang="en">
<head>
<meta charset="utf-8">
<title>Corvane Supplies Business Card</title>
<link href="https://fonts.googleapis.com/css2?family=Jost:wght@400;500;600&display=swap" rel="stylesheet">
<style>
  :root {
    --bg: #dcdde0;
    --card: #ffffff;
    --red: #ec1c24;
    --cyan: #1fb3d6;
    --ink: #4a4a4a;
    --shadow: rgba(0,0,0,0.18);
  }
  * { margin: 0; padding: 0; box-sizing: border-box; }
  html, body { width: 1200px; height: 800px; overflow: hidden; }
  body {
    background: var(--bg);
    font-family: "Jost", sans-serif;
    display: flex;
    align-items: center;
    justify-content: center;
    gap: 60px;
  }
  .card {
    position: relative;
    width: 525px;
    height: 300px;
    background: var(--card);
    box-shadow: 0 6px 18px var(--shadow);
    overflow: hidden;
  }
  .card__band {
    position: absolute;
    left: 0;
    bottom: 18px;
    width: 100%;
    height: 26px;
  }
  .brand {
    position: absolute;
    right: 34px;
    bottom: 74px;
    display: flex;
    align-items: center;
    gap: 10px;
  }
  .brand__mark {
    width: 22px;
    height: 22px;
    background: var(--red);
  }
  .brand__name {
    font-weight: 600;
    font-size: 22px;
    letter-spacing: 1px;
    color: var(--red);
    text-transform: uppercase;
  }
  .back__web {
    position: absolute;
    top: 26px;
    left: 34px;
    font-size: 14px;
    font-weight: 500;
    letter-spacing: 1.5px;
    color: var(--cyan);
  }
  .front__person { position: absolute; top: 26px; left: 34px; }
  .person__name {
    font-size: 18px;
    font-weight: 600;
    color: var(--cyan);
    letter-spacing: 1px;
    text-transform: uppercase;
    border-bottom: 1.5px solid var(--red);
    padding-bottom: 2px;
    display: inline-block;
    padding-right: 16px;
  }
  .person__role { font-size: 13px; color: var(--ink); margin-top: 2px; }
  .contact { list-style: none; margin-top: 12px; }
  .contact__item {
    display: flex;
    align-items: center;
    gap: 8px;
    font-size: 13px;
    color: var(--ink);
    line-height: 19px;
  }
  .contact__icon { width: 11px; height: 11px; flex: none; }
  .address {
    font-style: normal;
    font-size: 14px;
    color: var(--ink);
    margin-top: 10px;
    line-height: 19px;
  }
</style>
</head>
<body>

  <section class="card card--back" aria-label="Card back">
    <div class="back__web">www.corvanesupplies.com</div>
    <div class="brand">
      <span class="brand__mark"></span>
      <span class="brand__name">Corvane Supplies</span>
    </div>
    <svg class="card__band" viewBox="0 0 525 26" preserveAspectRatio="none" aria-hidden="true">
      <polygon points="0,0 185,0 178,12 0,12" fill="var(--cyan)"/>
      <polygon points="190,0 525,0 525,26 176,26" fill="var(--red)"/>
    </svg>
  </section>

  <section class="card card--front" aria-label="Card front">
    <div class="front__person">
      <div class="person__name">Dale Harmon</div>
      <div class="person__role">Director</div>
      <ul class="contact">
        <li class="contact__item">
          <svg class="contact__icon" viewBox="0 0 12 12"><rect x="3" y="0.5" width="6" height="11" rx="1" fill="none" stroke="var(--red)" stroke-width="1.2"/></svg>
          300-555-0142
        </li>
        <li class="contact__item">
          <svg class="contact__icon" viewBox="0 0 12 12"><path d="M2 1 L4.5 1 L5.5 3.8 L4 5 Q5.2 7.3 7 8 L8.2 6.5 L11 7.5 L11 10 Q6 11.5 2.5 7 Q0.5 4 2 1Z" fill="var(--red)"/></svg>
          (832)555-0187
        </li>
        <li class="contact__item">
          <svg class="contact__icon" viewBox="0 0 12 12"><rect x="0.5" y="2" width="11" height="8" fill="var(--red)"/><path d="M0.5 2 L6 6.5 L11.5 2" fill="none" stroke="#fff" stroke-width="1"/></svg>
          sales@corvanesupplies.com
        </li>
        <li class="contact__item">
          <svg class="contact__icon" viewBox="0 0 12 12"><circle cx="6" cy="6" r="5" fill="none" stroke="var(--red)" stroke-width="1.2"/><path d="M1 6 H11 M6 1 V11" stroke="var(--red)" stroke-width="1"/></svg>
          www.corvanesupplies.com
        </li>
      </ul>
      <address class="address">415 N.Calloway Suite 2<br>Midland, Tx 79701</address>
    </div>
    <div class="brand">
      <span class="brand__mark"></span>
      <span class="brand__name">Corvane Supplies</span>
    </div>
    <svg class="card__band" viewBox="0 0 525 26" preserveAspectRatio="none" aria-hidden="true">
      <polygon points="0,0 330,0 314,26 0,26" fill="var(--red)"/>
      <polygon points="340,14 525,14 525,26 333,26" fill="var(--cyan)"/>
    </svg>
  </section>

</body>
</html>
```